Fitness Body Weight Exercises Book Cover

Need a book cover design for a new book

This book is going to market to people to get in shape by playing a fitness dice game call FlexTRIO The dice game

When people see the cover they should see that this is a book that can help them get in shape. We are positioning the guru as an expert inside of the fitness niche

Target Market(s)

fitness

Requirements
Must have
• The name of the book which is

"The Grand Summit Frame Regimen"

Tagline -

The Worlds #1 Resource For Combat Strength Training Using Body Weight Exercises For Men, Women and Children

__________

Featuring FlexTRIO The Dice Game (TM)

___________________________
ON THE BACK COVER

Image with Oren with his gold medal
with these words
No Weights, No Problem

_____-

front cover
the image with him doing a push up should be on the front of the cover with these words

_________
Nice to have
• Maybe

"Oren Presents ...."

The Grand Summit Frame Regimen

```html
<!DOCTYPE html>
<html lang="en">
<head>
<meta charset="utf-8">
<title>The Grand Summit Frame Regimen – Book Cover</title>
<link rel="stylesheet" href="https://fonts.googleapis.com/css2?family=Anton&family=Montserrat:wght@500;600;700&display=swap">
<style>
  :root {
    --page-bg: #efefef;
    --cover-dark: #1a0204;
    --cover-mid: #5a0b10;
    --cover-red: #d0202a;
    --flame-core: #f7a21b;
    --flame-edge: #c2340f;
    --skin-light: #b07a55;
    --skin-dark: #5c3522;
    --band-orange: #e69324;
    --band-red: #c8232c;
    --ink-dark: #2a1206;
    --ink-light: #ffffff;
    --label-black: #0b0b0b;
    --photo-grey: #4a4a48;
    --photo-ground: #8a8a86;
  }
  * { box-sizing: border-box; margin: 0; padding: 0; }
  html, body {
    width: 1200px; height: 736px; overflow: hidden;
    background: var(--page-bg);
  }
  .stage { position: relative; width: 1200px; height: 736px; }

  .cover {
    position: absolute; top: 80px;
    width: 460px; height: 575px; overflow: hidden;
    box-shadow: 0 8px 24px rgba(0,0,0,.25);
  }

  /* ---------- Front cover ---------- */
  .front-cover {
    left: 110px;
    background:
      radial-gradient(ellipse 70% 55% at 45% 35%, var(--cover-red) 0%, var(--cover-mid) 55%, var(--cover-dark) 100%);
  }
  .flame-art {
    position: absolute; left: 0; top: 50px; width: 270px; height: 380px;
    background: radial-gradient(ellipse 55% 60% at 55% 55%, var(--flame-core) 0%, var(--flame-edge) 50%, rgba(120,20,10,0) 80%);
  }
  .champion-photo {
    position: absolute; left: 50px; top: 190px; width: 330px; height: 385px;
    border-radius: 120px 120px 0 0;
    background: linear-gradient(180deg, var(--skin-light) 0%, var(--skin-dark) 100%);
  }
  .presenter-label {
    position: absolute; left: 232px; top: 30px;
    background: var(--label-black); color: var(--ink-light);
    font: 600 15px/1 "Montserrat", sans-serif;
    padding: 7px 12px;
  }
  .book-title {
    position: absolute; right: 22px; top: 62px;
    color: var(--ink-light); text-align: right;
    font: 400 41px/44px "Anton", sans-serif;
    text-shadow: 3px 3px 0 #000;
  }
  .tagline-band {
    position: absolute; right: 0; top: 252px; width: 250px; height: 100px;
    background: var(--band-orange);
    color: var(--ink-dark); text-align: right;
    font: 600 12.5px/15px "Montserrat", sans-serif;
    padding: 6px 16px 0 10px;
  }
  .feature-band {
    position: absolute; right: 0; top: 352px; width: 225px; height: 86px;
    background: var(--band-red);
    color: var(--ink-light); text-align: right;
    font: 700 19px/24px "Montserrat", sans-serif;
    padding: 8px 14px 0 0;
  }
  .feature-band sup { font-size: 10px; }

  /* ---------- Back cover ---------- */
  .back-cover {
    left: 640px;
    background:
      radial-gradient(ellipse 62% 58% at 50% 42%, var(--cover-red) 0%, var(--cover-mid) 45%, var(--cover-dark) 90%);
  }
  .back-blurb {
    position: absolute; left: 71px; top: 73px; width: 274px;
    color: var(--ink-light); text-align: justify;
    font: 500 11px/14px "Montserrat", sans-serif;
  }
  .pushup-photo {
    position: absolute; left: 71px; top: 237px; width: 272px; height: 181px;
    background: linear-gradient(180deg, var(--photo-grey) 0%, #5a4638 50%, var(--photo-ground) 100%);
  }
  .back-caption {
    position: absolute; left: 0; right: 0; top: 432px;
    text-align: center; color: var(--ink-light);
    font: 400 16px/1 "Anton", sans-serif; letter-spacing: .2px;
  }
  .back-footnote {
    position: absolute; left: 70px; top: 484px; width: 150px;
    color: var(--ink-light);
    font: 500 9px/11.5px "Montserrat", sans-serif;
  }
</style>
</head>
<body>
<main class="stage">

  <section class="cover front-cover">
    <div class="flame-art" role="img" aria-label="Burning flames behind the champion"></div>
    <div class="champion-photo" role="img" aria-label="Oren smiling, shirtless, wearing his gold medal"></div>

    <div class="presenter-label">Oren presents :</div>
    <h1 class="book-title">"The Grand<br>Summit<br>Frame<br>Regimen"</h1>

    <p class="tagline-band">
      The Worlds #1 Resource<br>
      For Combat Strength<br>
      Training Using<br>
      Body Weight Exercises<br>
      For Men, Women<br>
      and Children
    </p>

    <p class="feature-band">
      Featuring<br>
      FlexTRIO<br>
      The Dice Game<sup>TM</sup>
    </p>
  </section>

  <section class="cover back-cover">
    <p class="back-blurb">Lorem ipsum dolor sit amet, consectetur adipiscing elit, sed do eiusmod tempor incididunt ut labore et dolore magna aliqua. Ut enim ad minim veniam, quis nostrud exercitation ullamco laboris nisi ut aliquip ex ea commodo consequat. Duis aute irure dolor in reprehenderit in voluptate velit esse cillum dolore eu fugiat nulla pariatur. Excepteur sint occaecat cupidatat non proident, sunt in culpa qui officia deserunt mollit anim id est laborum.</p>

    <div class="pushup-photo" role="img" aria-label="Oren doing a push-up on a concrete floor"></div>

    <p class="back-caption">No Weights, No Problem</p>

    <p class="back-footnote">Lorem ipsum dolor sit amet, consectetur adipiscing elit, sed do eiusmod tempor</p>
  </section>

</main>
</body>
</html>
```